A clean crisp business card for a Landscape Construction company. Designed to be easy to read contact/ info and also be appealing/interesting, unlike a traditional business card.

Industry/Entity Type

Landscape Construction

Contact Information for Business Card

Company name : Bramblecrest Landscape Construction, phone number: (877) 62Vales, website:Bramblecrestlandscapes.example, Email, sales@bramblecrestlandscapes.example

Requirements
Nice to have
• Luxurious finishes/ details…. Icons or emblems next to contact info
Should not have
• Clipart or general pictures

```html
<!DOCTYPE html>
<html lang="en">
<head>
<meta charset="utf-8">
<title>Bramblecrest Landscape Construction – Business Card</title>
<link href="https://fonts.googleapis.com/css2?family=Montserrat:wght@400;500;600&display=swap" rel="stylesheet">
<style>
  :root {
    --backdrop: #f1f8fb;
    --card: #ffffff;
    --blue: #2a6fbb;
    --green: #9acb3c;
    --ink: #1d1d1f;
    --leaf: #e3e9ef;
  }
  * { margin: 0; padding: 0; box-sizing: border-box; }
  html, body { width: 1200px; height: 459px; overflow: hidden; }
  body {
    background: var(--backdrop);
    font-family: "Montserrat", sans-serif;
    position: relative;
  }
  .card {
    position: absolute;
    top: 101px;
    width: 452px;
    height: 258px;
    background: var(--card);
    overflow: hidden;
    box-shadow: 0 14px 28px rgba(0,0,0,0.28);
  }
  .card--front { left: 130px; }
  .card--back { left: 618px; }

  .leaf-decor {
    position: absolute;
    background: radial-gradient(ellipse at center, var(--leaf) 0%, rgba(227,233,239,0.6) 55%, rgba(227,233,239,0) 72%);
  }
  .card--front .leaf-decor { left: 0; top: 100px; width: 175px; height: 158px; }
  .card--back .leaf-decor { right: 0; top: 0; width: 170px; height: 160px; }

  .stripes { position: absolute; left: 0; bottom: 0; width: 452px; height: 20px; }

  .brand {
    position: absolute;
    text-align: center;
    color: var(--blue);
    font-weight: 600;
  }
  .brand__name { display: block; letter-spacing: 0.5px; }
  .brand__tagline { display: block; font-weight: 600; letter-spacing: 2px; text-transform: uppercase; }

  .card--front .brand { left: 0; width: 452px; top: 142px; }
  .card--front .brand__name { font-size: 30px; line-height: 34px; }
  .card--front .brand__tagline { font-size: 10px; margin-top: 4px; letter-spacing: 3px; }

  .card--back .brand { left: 8px; width: 190px; top: 140px; }
  .card--back .brand__name { font-size: 18px; line-height: 22px; }
  .card--back .brand__tagline { font-size: 6px; letter-spacing: 1.3px; margin-top: 2px; }

  .divider {
    position: absolute; left: 203px; top: 59px;
    width: 2px; height: 138px; background: var(--blue);
  }
  .heading {
    position: absolute; left: 220px; top: 58px;
    color: var(--blue);
  }
  .heading__name { display: block; font-size: 21px; font-weight: 400; line-height: 24px; }
  .heading__tagline { display: block; font-size: 7.5px; font-weight: 400; text-transform: uppercase; margin-top: 1px; }

  .contacts { position: absolute; left: 220px; top: 135px; list-style: none; }
  .contact {
    display: flex; align-items: center; height: 23.5px;
    font-size: 9px; color: var(--ink); letter-spacing: 0.3px;
  }
  .contact__icon {
    width: 14px; height: 14px; border-radius: 50%;
    background: var(--blue); margin-right: 7px; flex: none;
    display: flex; align-items: center; justify-content: center;
  }
</style>
</head>
<body>

<section class="card card--front">
  <div class="leaf-decor" role="img" aria-label="Faint leaf decoration"></div>
  <div class="brand">
    <span class="brand__name">Bramblecrest</span>
    <span class="brand__tagline">Landscape Construction</span>
  </div>
  <svg class="stripes" viewBox="0 0 452 20" aria-hidden="true">
    <polygon points="0,4 340,5 335,12 0,12" fill="var(--green)"/>
    <polygon points="347,6 452,6 452,13 343,13" fill="var(--blue)"/>
  </svg>
</section>

<section class="card card--back">
  <div class="leaf-decor" role="img" aria-label="Faint leaf decoration"></div>
  <div class="brand">
    <span class="brand__name">Bramblecrest</span>
    <span class="brand__tagline">Landscape Construction</span>
  </div>
  <div class="divider"></div>
  <div class="heading">
    <span class="heading__name">Bramblecrest</span>
    <span class="heading__tagline">Landscape Construction</span>
  </div>
  <ul class="contacts">
    <li class="contact">
      <span class="contact__icon">
        <svg width="8" height="8" viewBox="0 0 24 24"><path fill="#fff" d="M6.6 10.8a15 15 0 0 0 6.6 6.6l2.2-2.2c.3-.3.7-.4 1-.2 1.1.4 2.3.6 3.6.6.6 0 1 .4 1 1V20c0 .6-.4 1-1 1A17 17 0 0 1 3 4c0-.6.4-1 1-1h3.5c.6 0 1 .4 1 1 0 1.3.2 2.5.6 3.6.1.3 0 .7-.2 1z"/></svg>
      </span>(877) 62Vales
    </li>
    <li class="contact">
      <span class="contact__icon">
        <svg width="9" height="9" viewBox="0 0 24 24" fill="none" stroke="#fff" stroke-width="2"><circle cx="12" cy="12" r="9"/><path d="M3 12h18M12 3c3 3 3 15 0 18M12 3c-3 3-3 15 0 18"/></svg>
      </span>Bramblecrestlandscapes.example
    </li>
    <li class="contact">
      <span class="contact__icon">
        <svg width="9" height="9" viewBox="0 0 24 24" fill="none" stroke="#fff" stroke-width="2"><rect x="3" y="6" width="18" height="12"/><path d="M3 6l9 7 9-7"/></svg>
      </span>sales@bramblecrestlandscapes.example
    </li>
  </ul>
  <svg class="stripes" viewBox="0 0 452 20" aria-hidden="true">
    <polygon points="0,4 340,5 335,12 0,12" fill="var(--green)"/>
    <polygon points="347,6 452,6 452,13 343,13" fill="var(--blue)"/>
  </svg>
</section>

</body>
</html>
```